Modernise Business Card

Our company has been operating for 10 years. With the start of the new decade we are looking to refresh our business card design. We manufacture a range of industrial product shipping to customers internationally. A copy of our current card, both sides, is attached. We are looking for a mature professional appearance.

```html
<!DOCTYPE html>
<html lang="en">
<head>
<meta charset="utf-8">
<title>Korvane Business Card – Front and Back</title>
<link rel="stylesheet" href="https://fonts.googleapis.com/css2?family=Source+Sans+3:wght@400;600;700&display=swap">
<style>
  :root {
    --stage: #4b5053;
    --card: #232325;
    --brand-blue: #1e9bd7;
    --text-light: #f2f2f2;
    --rule: #5a5a5e;
    --icon-bg: #ffffff;
  }
  * { box-sizing: border-box; margin: 0; padding: 0; }
  html, body {
    width: 1200px; height: 1050px; overflow: hidden;
    background: var(--stage);
    font-family: "Source Sans 3", "Myriad Pro", sans-serif;
  }
  .stage {
    position: relative; width: 1200px; height: 1050px;
  }
  .card {
    position: absolute; left: 280px;
    width: 640px; height: 390px;
    background: var(--card);
    box-shadow: 0 10px 30px rgba(0,0,0,.35);
    overflow: hidden;
  }
  .card--front { top: 105px; }
  .card--back  { top: 555px; }

  .wordmark {
    position: absolute;
    color: var(--brand-blue);
    font-weight: 700;
    letter-spacing: -1px;
    line-height: 1;
  }
  .card--front .wordmark { left: 150px; top: 22px; font-size: 92px; }
  .card--back  .wordmark { left: 0; right: 0; top: 150px; text-align: center; font-size: 112px; }

  .holder-name {
    position: absolute; left: 155px; top: 120px;
    color: var(--text-light); font-size: 38px; font-weight: 400;
  }
  .contact-list { position: absolute; left: 152px; top: 172px; list-style: none; }
  .contact-item {
    display: flex; align-items: center; height: 39px;
    color: var(--text-light); font-size: 23px;
  }
  .contact-icon {
    width: 26px; height: 26px; margin-right: 10px; flex: none;
  }
  .contact-label { color: var(--brand-blue); margin-right: 10px; }

  .divider {
    position: absolute; left: 24px; right: 24px; top: 333px;
    border-top: 1px solid var(--rule);
  }
  .address {
    position: absolute; left: 28px; top: 348px;
    display: flex; align-items: center;
    color: var(--brand-blue); font-size: 16.5px; white-space: nowrap;
  }
  .address svg { width: 20px; height: 20px; margin-right: 8px; flex: none; }

  .tagline {
    position: absolute; left: 0; right: 0; top: 282px;
    text-align: center; color: var(--text-light); font-size: 25px;
    word-spacing: 1px;
  }
  .tagline .sep { margin: 0 14px; }
</style>
</head>
<body>
<main class="stage">

  <section class="card card--front" aria-label="Business card front">
    <div class="wordmark">Korvane</div>
    <h1 class="holder-name">Alan Pierce</h1>
    <ul class="contact-list">
      <li class="contact-item">
        <svg class="contact-icon" viewBox="0 0 26 26" aria-hidden="true">
          <circle cx="13" cy="13" r="13" fill="var(--icon-bg)"/>
          <path d="M7 10c0-2 3-3 6-3s6 1 6 3v1h-3V9.5h-6V11H7z M9 12h8l1.5 6h-11z" fill="var(--brand-blue)"/>
          <circle cx="13" cy="15" r="1.6" fill="var(--icon-bg)"/>
        </svg>
        <span class="contact-label">Australia</span>+61 400 555 018
      </li>
      <li class="contact-item">
        <svg class="contact-icon" viewBox="0 0 26 26" aria-hidden="true">
          <circle cx="13" cy="13" r="13" fill="var(--icon-bg)"/>
          <path d="M7 10c0-2 3-3 6-3s6 1 6 3v1h-3V9.5h-6V11H7z M9 12h8l1.5 6h-11z" fill="var(--brand-blue)"/>
          <circle cx="13" cy="15" r="1.6" fill="var(--icon-bg)"/>
        </svg>
        <span class="contact-label">China</span>+86 139 0000 4521
      </li>
      <li class="contact-item">
        <svg class="contact-icon" viewBox="0 0 26 26" aria-hidden="true">
          <circle cx="13" cy="13" r="13" fill="var(--icon-bg)"/>
          <g fill="none" stroke="var(--brand-blue)" stroke-width="1.5">
            <circle cx="13" cy="13" r="7.5"/>
            <ellipse cx="13" cy="13" rx="3.5" ry="7.5"/>
            <line x1="5.5" y1="13" x2="20.5" y2="13"/>
            <line x1="7" y1="9" x2="19" y2="9"/>
            <line x1="7" y1="17" x2="19" y2="17"/>
          </g>
        </svg>
        <span>www.korvanefittings.com</span>
      </li>
      <li class="contact-item">
        <svg class="contact-icon" viewBox="0 0 26 26" aria-hidden="true">
          <circle cx="13" cy="13" r="13" fill="var(--icon-bg)"/>
          <rect x="6.5" y="8.5" width="13" height="9" fill="var(--brand-blue)"/>
          <path d="M6.5 8.5l6.5 5 6.5-5" fill="none" stroke="var(--icon-bg)" stroke-width="1.3"/>
        </svg>
        <span>apierce@korvanefittings.com</span>
      </li>
    </ul>
    <div class="divider"></div>
    <p class="address">
      <svg viewBox="0 0 20 20" aria-hidden="true">
        <rect width="20" height="20" fill="var(--icon-bg)"/>
        <path d="M10 3a4 4 0 0 1 4 4c0 3-4 7-4 7s-4-4-4-7a4 4 0 0 1 4-4z" fill="var(--brand-blue)"/>
        <circle cx="10" cy="7" r="1.5" fill="var(--icon-bg)"/>
        <ellipse cx="10" cy="16" rx="6" ry="1.6" fill="none" stroke="var(--brand-blue)" stroke-width="1.2"/>
      </svg>
      88-4 , Lian Feng Building 120 Harbour Road , Jiangbei District Ningbo 315000 China
    </p>
  </section>

  <section class="card card--back" aria-label="Business card back">
    <div class="wordmark">Korvane</div>
    <p class="tagline">Hydraulic Adapters<span class="sep">|</span>Hose Fittings<span class="sep">|</span>Quick Couplings</p>
  </section>

</main>
</body>
</html>
```